Bright Meadow LLC business card

I help with the Marketing and Sales of various Natural, Organic, Eco Friendly and Healthy Main Stream products to Retail Corporate accounts as well as Independents and Distributors.I also highlight Private label items to these same Retail Corporate accounts.Cherish the Moments, Enjoy Life!

Speciality & Health Sales and Marketing

Target Market(s)

Men and Women

Industry/Entity Type

Business

Contact Information for Business Card

Bright Meadow, LLC
Janet Lou Brindall
418 West Fern Lane
Ste 3-274
Phoenix, AZ 85047
602-555-0173
jbrindall@veltramail.net

Requirements
Must have
• Nice, femine font
Something in the background or on a side with a softness
Nice to have
• Cherish the Moments, Enjoy Life
Should not have
• Hardness

```html
<!DOCTYPE html>
<html lang="en">
<head>
<meta charset="utf-8">
<title>Bright Meadow LLC – Business Card</title>
<link href="https://fonts.googleapis.com/css2?family=Italianno&family=Barlow:wght@500&display=swap" rel="stylesheet">
<style>
  :root {
    --backdrop: #ececec;
    --leaf-light: #f4f25a;
    --leaf-mid: #c6e234;
    --leaf-deep: #7fbf1e;
    --glow: #fffbd0;
    --ink: #1c1c14;
    --rule: #3a3a2a;
  }
  html, body {
    margin: 0;
    width: 1200px;
    height: 963px;
    overflow: hidden;
    background: var(--backdrop);
  }
  .business-card {
    position: absolute;
    left: 150px;
    top: 224px;
    width: 900px;
    height: 514px;
    overflow: hidden;
    box-shadow: 0 10px 30px rgba(0,0,0,0.12);
  }
  .leaf-backdrop {
    position: absolute;
    inset: 0;
    background:
      radial-gradient(ellipse 45% 55% at 22% 30%, var(--glow) 0%, rgba(255,251,208,0) 70%),
      radial-gradient(ellipse 40% 70% at 72% 45%, rgba(214,236,70,0.9) 0%, rgba(214,236,70,0) 75%),
      radial-gradient(ellipse 50% 50% at 90% 90%, rgba(110,180,25,0.8) 0%, rgba(110,180,25,0) 70%),
      linear-gradient(160deg, var(--leaf-light) 0%, var(--leaf-mid) 45%, var(--leaf-deep) 100%);
  }
  .card-text {
    position: absolute;
    left: 0;
    top: 100px;
    width: 560px;
  }
  .brand-name {
    margin: 0;
    padding-left: 70px;
    font-family: "Italianno", cursive;
    font-weight: 400;
    font-size: 96px;
    line-height: 1;
    color: var(--ink);
  }
  .brand-rule {
    width: 100%;
    height: 0;
    border-top: 2px dotted var(--rule);
    margin: 2px 0 14px;
  }
  .contact-lines {
    margin: 0;
    padding-left: 100px;
    font-family: "Barlow", sans-serif;
    font-weight: 500;
    font-size: 30px;
    line-height: 1.42;
    color: var(--ink);
  }
</style>
</head>
<body>
  <section class="business-card">
    <div class="leaf-backdrop" role="img" aria-label="Soft close-up photograph of fresh green and yellow leaves in glowing light"></div>
    <div class="card-text">
      <h1 class="brand-name">Bright Meadow</h1>
      <div class="brand-rule"></div>
      <p class="contact-lines">LLC Janet Lou Brindall 418<br>West Fern Lane Ste 3-274 Phoenix,<br>AZ 85047</p>
    </div>
  </section>
</body>
</html>
```